Photography and Videography - Brightwell Studios - New Business Card Design

Brightwell Studios is a photography and Videography Company started by creative couple Robby K and Lenna P and based on the Sunshine Coast in Queensland, Australia.
We're quirky, creative and innovative people and would like a business card that keeps you looking for more than just a few seconds.
Design wise we would like a black or charcoal background with a bit of a funkier design than just a boring old rectangle shape. Perhaps curved on an edge.
Ideally we would like to be able to make a collage of all of our best photos on the reverse side of the card with the company name or logo and "catch you round the bend..." (possibly in italics) underneath it.
On the front of the business card we would like our company name -
"Brightwell Studios", our motto- "Bringing Ideas To Life..." (possibly in italics) and our contact information. The background should be a darker colour like black or charcoal.
We like the look of having contact company details and contact info to one side (right) and a black and white photo of Robby K and Lenna P to the other side (left).
Thank you and Good Luck!
Industry/Entity Type
Business
Contact Information for Business Card
Business Name - Brightwell Studios
Slogan - Bring Ideas To life
Name - Robby K | Lenna P
Description - Photography | Videography
Phone - 0438 526 017 | 0412 873 205
Email - brightwellstudios@mailbox.com.au
Website - www.brightwellstudios.com.au
Logo styles of interest
Pictorial/Combination Logo
Look and feel

```html
<!DOCTYPE html>
<html lang="en">
<head>
<meta charset="utf-8">
<title>Brightwell Studios – Business Card</title>
<link href="https://fonts.googleapis.com/css2?family=Mulish:ital,wght@0,400;0,800;1,400&display=swap" rel="stylesheet">
<style>
  :root {
    --bg: #e9e6e1;
    --card: #3a3a3a;
    --card-dark: #2e2e2e;
    --title: #f3ebc4;
    --accent: #eadfa6;
    --muted: #c9c2a2;
    --faint: #7d7b74;
    --icon: #4a6fa8;
  }
  * { margin: 0; padding: 0; box-sizing: border-box; }
  html, body { width: 1200px; height: 871px; overflow: hidden; background: var(--bg); }
  body { position: relative; font-family: "Mulish", sans-serif; }

  .card {
    position: absolute;
    top: 125px;
    width: 380px;
    height: 620px;
    background: linear-gradient(160deg, var(--card) 0%, var(--card-dark) 100%);
    box-shadow: 0 10px 30px rgba(0,0,0,.25);
    overflow: hidden;
  }
  .card--front { left: 170px; }
  .card--back  { left: 650px; }

  /* front */
  .brand { position: absolute; left: 28px; top: 40px; }
  .brand__name {
    font-weight: 800; font-size: 25px; letter-spacing: .5px;
    color: var(--title); text-transform: uppercase; white-space: nowrap;
  }
  .brand__motto {
    font-style: italic; font-size: 13px; letter-spacing: 2px;
    color: var(--muted); margin-left: 44px; margin-top: 1px;
  }
  .portrait {
    position: absolute; right: 26px; top: 92px; width: 128px; height: 138px;
    background: linear-gradient(135deg, #cfcfcf 0%, #7a7a7a 55%, #2a2a2a 100%);
    border: 2px solid #222;
  }
  .names {
    position: absolute; left: 28px; top: 112px;
    font-size: 22px; line-height: 26px; color: var(--accent);
  }
  .phones {
    position: absolute; left: 52px; top: 252px;
    font-size: 23px; line-height: 30px; letter-spacing: 1.5px; color: #fff8dc;
  }
  .web {
    position: absolute; left: 44px; top: 346px;
    font-size: 15.5px; line-height: 26px; color: var(--muted); font-style: italic;
  }
  .services {
    position: absolute; left: 0; right: 0; top: 468px; text-align: center;
    font-size: 22px; color: var(--accent);
  }
  .social {
    position: absolute; left: 0; right: 0; bottom: 30px;
    display: flex; justify-content: center; align-items: center; gap: 8px;
    font-size: 19px; color: var(--faint);
  }
  .social__mark { width: 18px; height: 18px; background: var(--icon); border-radius: 3px; }

  /* back */
  .back__head {
    position: absolute; left: 0; right: 0; top: 0; height: 220px;
    display: flex; align-items: center; justify-content: center;
  }
  .back__logo {
    writing-mode: vertical-rl;
    font-weight: 800; font-size: 21px; letter-spacing: 2px; line-height: 1;
    color: var(--accent); text-transform: uppercase; white-space: nowrap;
  }
  .collage {
    position: absolute; left: 0; right: 0; top: 220px; bottom: 0;
    background:
      linear-gradient(160deg, rgba(70,140,210,.85) 0%, rgba(120,170,90,.75) 35%, rgba(230,120,40,.85) 65%, rgba(150,120,90,.8) 100%);
  }
</style>
</head>
<body>
  <section class="card card--front">
    <div class="brand">
      <div class="brand__name">Brightwell Studios</div>
      <div class="brand__motto">Bring ideas to life!</div>
    </div>
    <div class="portrait" role="img" aria-label="Black and white photo of Robby K and Lenna P"></div>
    <div class="names">Robby K<br>Lenna P</div>
    <div class="phones">0438 526 017<br>0412 873 205</div>
    <div class="web">brightwellstudios@mailbox.com.au<br>www.brightwellstudios.com.au</div>
    <div class="services">Photography | Videography</div>
    <div class="social">Like us on Linkwall <span class="social__mark"></span></div>
  </section>

  <section class="card card--back">
    <div class="back__head">
      <div class="back__logo">Brightwell</div>
    </div>
    <div class="collage" role="img" aria-label="Collage of the studio's best photographs: beaches, sunsets, flowers and couples"></div>
  </section>
</body>
</html>
```